Simple psychologist website
Open brief, creative designs encouraged
Site map:
Home
our services
our psychologists
selective mutism
resources
contact

Current website:
http://mindsproutyouth.com.au/
Not in love with our logo, or colours etc - open brief
Happy for new font/style/logo for company name - if we choose a logo design from a designer who doesn't win the competition, we will award $50 for the logo and use it in the new website

Website made a few years ago for a sister company that we really like:
http://www.korrelpsychology.com.au/

Clean, credible and warm and friendly look & feel
stock photos OK, designer will be required to hand over any images used in the design as shown in the PSD

Target Market(s)

Adolescents with psychological issues and their families

Industry/Entity Type

Psychology

Number of Pages Required

2 page

Colors

Designer to choose colors to be used in the design.

Requirements
Must have
• One home page - simple with 2 or 3 small areas to tease and attract the user and one template page to suit all the other pages
• We like slides, we want to have 3 slides like korrelpsychology.com.au
• Three slide titles:
• 1. We specialise in many areas, find the right clinical psychologist for your family
• 2. Child Clinical Psychologists in Chatswood and Westmead
• 3. Resources
• Pages structurally similar to
• http://www.korrelpsychology.com.au/
• We like the 'featured' items, which in our case will have splash box titles (can be 3 or 4):
• 1. Selective Mutism
• 2. Is my child anxious?
• 3. Does my child have an eating disorder?
• 4. Parenting adolescents
• Does not need to be a copy of http://www.korrelpsychology.com.au/ and we are willing to accept outside-the-box thinking and design (we in fact encourage it)
• Owner of business wants to highlight Selective Mutism as they have specialists. Consider ways that may make this work.
• Design winner will be based on home page design but winning designer will be required to provide an additional but simpler 'standard' page template design based on the themes used in the winning design.

```html
<!DOCTYPE html>
<html lang="en">
<head>
<meta charset="utf-8">
<title>Mindsprout – Child, Adolescent &amp; Family Psychology</title>
<link href="https://fonts.googleapis.com/css2?family=Maven+Pro:wght@400;500;600;700&family=Arimo:wght@400;700&family=Roboto+Condensed:wght@400&display=swap" rel="stylesheet">
<style>
  :root {
    --blue: #2f9fd4;
    --ink: #2b2b2b;
    --text: #3c3c3c;
    --muted: #666;
    --tab-grey: #6f6f6f;
    --footer-grey: #5e5e5e;
    --footer-dark: #3a3a3a;
    --white: #ffffff;
  }
  * { box-sizing: border-box; margin: 0; padding: 0; }
  html, body { width: 910px; height: 1200px; overflow: hidden; background: var(--white); }
  body { position: relative; font-family: "Arimo", Arial, sans-serif; color: var(--text); }

  .site-header { position: absolute; left: 0; top: 0; width: 910px; height: 93px; border-top: 2px solid #6a6a6a; }
  .top-tabs { position: absolute; top: 0; left: 456px; height: 22px; display: flex; }
  .tab-offices { background: var(--tab-grey); color: var(--white); font: 600 8.2px "Maven Pro", sans-serif; line-height: 22px; width: 178px; padding-left: 16px; white-space: nowrap; clip-path: polygon(5% 0, 100% 0, 100% 100%, 0 100%); }
  .tab-phone { background: var(--blue); color: var(--white); font: 600 9.8px "Maven Pro", sans-serif; line-height: 22px; width: 152px; padding-left: 10px; display: flex; align-items: center; gap: 6px; white-space: nowrap; clip-path: polygon(0 0, 100% 0, 92% 100%, 0 100%); }
  .tab-phone svg { width: 13px; height: 13px; flex: none; }

  .brand { position: absolute; left: 124px; top: 24px; display: flex; align-items: center; gap: 8px; }
  .brand-dot { width: 48px; height: 48px; border-radius: 50%; background: var(--blue); }
  .brand-name { font: 600 21px "Maven Pro", sans-serif; color: var(--blue); line-height: 1; }
  .brand-tag { font: 400 8px "Roboto Condensed", sans-serif; color: var(--muted); margin-top: 2px; }

  .main-nav { position: absolute; top: 53px; left: 0; width: 910px; }
  .main-nav a { position: absolute; font: 500 10.4px "Maven Pro", sans-serif; color: #555; text-decoration: none; white-space: nowrap; }
  .main-nav a.active { color: var(--blue); }

  .hero { position: absolute; left: 0; top: 93px; width: 910px; height: 425px;
    background:
      radial-gradient(ellipse 220px 260px at 780px 210px, rgba(236,120,112,0.75), transparent 70%),
      radial-gradient(ellipse 180px 200px at 60px 130px, rgba(190,210,232,0.9), transparent 70%),
      radial-gradient(ellipse 170px 120px at 170px 80px, rgba(240,170,80,0.55), transparent 70%),
      radial-gradient(ellipse 200px 80px at 180px 370px, rgba(236,110,150,0.45), transparent 70%),
      linear-gradient(180deg, #f2ede6 0%, #f4efe9 70%, #e9e6e2 100%); }
  .hero-caption { position: absolute; left: 332px; top: 11px; width: 244px; height: 244px; border-radius: 50%; background: rgba(110,108,104,0.88); color: var(--white); text-align: center; padding-top: 58px; }
  .hero-caption h1 { font: 600 19.5px/28px "Maven Pro", sans-serif; }
  .hero-caption a { display: inline-block; margin-top: 15px; color: var(--white); font: 600 17px "Maven Pro", sans-serif; text-decoration: underline; }
  .hero-dots { position: absolute; left: 123px; top: 385px; display: flex; gap: 7px; }
  .hero-dots span { width: 10px; height: 10px; border-radius: 50%; background: var(--white); }
  .hero-dots span.on { background: var(--blue); border: 2px solid var(--white); }

  .welcome { position: absolute; top: 560px; left: 0; width: 910px; text-align: center; }
  .welcome h2 { font: 700 26px "Maven Pro", sans-serif; color: var(--blue); }
  .welcome .sub { font: 400 10px "Roboto Condensed", sans-serif; color: var(--muted); margin-top: -2px; }
  .welcome .lead { font: 400 11.8px "Arimo", sans-serif; color: var(--ink); margin-top: 18px; }
  .welcome .body { font: 400 8.8px/15px "Arimo", sans-serif; color: var(--text); width: 670px; margin: 10px auto 0; }
  .welcome .more { display: inline-block; margin-top: 10px; font: 500 10px "Maven Pro", sans-serif; color: var(--blue); text-decoration: underline; }

  .services-title { position: absolute; top: 766px; left: 0; width: 910px; text-align: center; font: 600 19px "Maven Pro", sans-serif; color: #666; }
  .services-title span { color: var(--blue); }
  .services-rule { position: absolute; top: 796px; left: 418px; width: 74px; height: 2px; background: var(--blue); }

  .service { position: absolute; top: 821px; width: 149px; text-align: center; }
  .service .photo { width: 149px; height: 91px; }
  .service .shadow { height: 6px; margin: 0 10px; background: radial-gradient(ellipse at top, rgba(0,0,0,0.14), transparent 70%); }
  .service h3 { font: 500 12.2px/15px "Maven Pro", sans-serif; color: var(--ink); margin-top: 12px; }
  .service p { font: 400 8.2px/12px "Arimo", sans-serif; color: var(--text); margin-top: 7px; }
  .service .plus { display: block; margin: 8px auto 0; width: 18px; height: 18px; }

  .footer-wave { position: absolute; left: 0; top: 1040px; width: 910px; height: 112px; }
  .footer-nav { position: absolute; top: 1123px; left: 0; width: 910px; }
  .footer-nav a { position: absolute; font: 400 9px "Maven Pro", sans-serif; color: #eee; text-decoration: none; white-space: nowrap; }
  .footer-nav a.active { color: var(--blue); }
  .footer-legal { position: absolute; top: 1127px; left: 632px; font: 400 9px "Maven Pro", sans-serif; color: #eee; display: flex; gap: 9px; }
  .footer-legal i { width: 1px; height: 12px; background: #bbb; }
  .footer-bottom { position: absolute; left: 0; top: 1152px; width: 910px; height: 48px; background: var(--footer-dark); color: var(--white); }
  .copyright { position: absolute; left: 126px; top: 17px; font: 400 9.5px "Maven Pro", sans-serif; }
  .follow { position: absolute; left: 630px; top: 13px; display: flex; align-items: center; gap: 4px; font: 400 10px "Maven Pro", sans-serif; }
  .follow .label { margin-right: 9px; }
  .social { width: 21px; height: 21px; border-radius: 50%; border: 1.5px solid var(--white); }
</style>
</head>
<body>

<header class="site-header">
  <div class="top-tabs">
    <div class="tab-offices">For Chatswood And Westmead Offices</div>
    <div class="tab-phone">
      <svg viewBox="0 0 16 16"><circle cx="8" cy="8" r="7" fill="none" stroke="#fff" stroke-width="1.2"/><path d="M5.5 4.5c.6-.4 1.2 0 1.3.6l.2 1c0 .4-.3.6-.6.8.3 1 .9 1.7 1.7 2.2.3-.3.5-.6.9-.5l1 .3c.6.2.8.8.4 1.3-.6.8-1.6.8-2.6.2-1.6-1-2.7-2.6-3-4.3 0-.7.1-1.3.7-1.6z" fill="#fff"/></svg>
      Call us on 0412 555 018
    </div>
  </div>

  <div class="brand">
    <div class="brand-dot"></div>
    <div>
      <div class="brand-name">MINDSPROUT</div>
      <div class="brand-tag">Child, Adolescent &amp; Family Psychology</div>
    </div>
  </div>

  <nav class="main-nav">
    <a class="active" style="left:346px">Home</a>
    <a style="left:392px">Our Services</a>
    <a style="left:469px;top:-1px">Our Psychologists</a>
    <a style="left:570px">Selective Mustim</a>
    <a style="left:668px">Resources</a>
    <a style="left:735px">Contact Us</a>
  </nav>
</header>

<section class="hero" role="img" aria-label="Photo of a therapist's hand playing a finger-walking game with a smiling young girl at a table, with a toy clock and children's paintings behind">
  <div class="hero-caption">
    <h1>Child Clinical<br>Psychologists in<br>Chatswood &amp; Westmead</h1>
    <a>More...</a>
  </div>
  <div class="hero-dots"><span></span><span class="on"></span><span></span></div>
</section>

<section class="welcome">
  <h2>WELCOME TO MINDSPROUT</h2>
  <div class="sub">Child, Adolescent &amp; Family Psychology</div>
  <p class="lead">We Provide Expert Treatment If Depression, Anxiety &amp; Eating Disorders</p>
  <p class="body">We are a group of clinical psychologists at Chatswood and Westmead (Sydney). We provide a range of services including the following:<br>Individual counselling and therapy for kids, teens and families, Family Consultations, Seminars and training with schools, Brief group programmes for anxiety, stress and body image concerns for adolescents.</p>
  <a class="more">Read More</a>
</section>

<h2 class="services-title"><span>OUR</span> SERVICES</h2>
<div class="services-rule"></div>

<article class="service" style="left:128px">
  <div class="photo" role="img" aria-label="Photo of a boy holding a handwritten greeting card" style="background:radial-gradient(ellipse 60px 40px at 75px 30px,#e2b48e,transparent 70%),linear-gradient(180deg,#7c5a3e 0%,#b88a62 45%,#e8e2d6 62%,#a77d5a 80%,#6b4a32 100%)"></div>
  <div class="shadow"></div>
  <h3>Selective<br>Mutism</h3>
  <p>Sed ut perspiciatis unde omnis iste natus error sit voluptatem accu santium doloremque.</p>
  <svg class="plus" viewBox="0 0 18 18"><path d="M1 4V1h16v3M1 14v3h16v-3" fill="none" stroke="#333" stroke-width="1.2"/><path d="M9 5v8M5 9h8" stroke="#333" stroke-width="1.6"/></svg>
</article>

<article class="service" style="left:296px">
  <div class="photo" role="img" aria-label="Photo of a worried girl sitting alone hugging her knees" style="background:radial-gradient(ellipse 45px 50px at 50px 45px,#caa57a,transparent 70%),linear-gradient(90deg,#5e4a3c 0%,#8c7258 40%,#6e5848 65%,#3e3029 100%)"></div>
  <div class="shadow"></div>
  <h3>Is My Child<br>Anxious?</h3>
  <p>Sed ut perspiciatis unde omnis iste natus error sit voluptatem accu santium doloremque.</p>
  <svg class="plus" viewBox="0 0 18 18"><path d="M1 4V1h16v3M1 14v3h16v-3" fill="none" stroke="#333" stroke-width="1.2"/><path d="M9 5v8M5 9h8" stroke="#333" stroke-width="1.6"/></svg>
</article>

<article class="service" style="left:465px">
  <div class="photo" role="img" aria-label="Photo of a boy refusing a plate of food at the table" style="background:radial-gradient(ellipse 40px 35px at 75px 50px,#9aa6b4,transparent 70%),linear-gradient(180deg,#f1efeb 0%,#e6e0d6 55%,#b89a72 75%,#6f7d4e 90%,#e4e0d8 100%)"></div>
  <div class="shadow"></div>
  <h3>Does My Child Have An<br>Eating Disorder?</h3>
  <p>Sed ut perspiciatis unde omnis iste natus error sit voluptatem accu santium doloremque.</p>
  <svg class="plus" viewBox="0 0 18 18"><path d="M1 4V1h16v3M1 14v3h16v-3" fill="none" stroke="#333" stroke-width="1.2"/><path d="M9 5v8M5 9h8" stroke="#333" stroke-width="1.6"/></svg>
</article>

<article class="service" style="left:633px">
  <div class="photo" role="img" aria-label="Photo of parents with a baby talking with a counsellor" style="background:radial-gradient(ellipse 35px 45px at 125px 60px,#4f6f9a,transparent 70%),radial-gradient(ellipse 40px 40px at 35px 60px,#c9a48a,transparent 70%),linear-gradient(90deg,#b8ad9c 0%,#e6e1d6 50%,#8b8e86 100%)"></div>
  <div class="shadow"></div>
  <h3>Parenting<br>Adolescents</h3>
  <p>Sed ut perspiciatis unde omnis iste natus error sit voluptatem accu santium doloremque.</p>
  <svg class="plus" viewBox="0 0 18 18"><path d="M1 4V1h16v3M1 14v3h16v-3" fill="none" stroke="#333" stroke-width="1.2"/><path d="M9 5v8M5 9h8" stroke="#333" stroke-width="1.6"/></svg>
</article>

<footer>
  <svg class="footer-wave" viewBox="0 0 910 112" preserveAspectRatio="none">
    <path d="M0 72 C200 20 420 10 600 30 C720 44 820 52 910 44 L910 112 L0 112 Z" fill="var(--footer-grey)"/>
    <path d="M0 60 C180 8 400 -4 600 18 C720 32 820 40 910 34 L910 42 C820 50 720 46 600 32 C420 14 200 22 0 70 Z" fill="var(--blue)"/>
    <path d="M0 70 C200 22 420 14 600 32 C720 46 820 50 910 42 L910 48 C820 58 720 56 600 42 C420 24 200 32 0 80 Z" fill="#ffffff"/>
  </svg>
  <nav class="footer-nav">
    <a class="active" style="left:122px">Home</a>
    <a style="left:168px">Our Services</a>
    <a style="left:241px;top:-1px">Our Psychologists</a>
    <a style="left:335px">Selective Mustim</a>
    <a style="left:426px">Resources</a>
    <a style="left:489px">Contact Us</a>
  </nav>
  <div class="footer-legal"><span>Privacy Policy</span><i></i><span>Terms &amp; Conditions</span></div>
  <div class="footer-bottom">
    <div class="copyright">Copyright © 2017 Mindsprout. All Rights Reserved.</div>
    <div class="follow">
      <span class="label">Follow Us</span>
      <span class="social"></span><span class="social"></span><span class="social"></span><span class="social"></span>
    </div>
  </div>
</footer>

</body>
</html>
```